Im open to ideas.. I was thinking on my business cards aswell as my logo. a place for my name. email. phone number and abn..

ive attched a file with my business logo. which i dont love the colours.. i was think a dark background with charcoal letters so something along those colour schumes but im open to ideas..

Business

BRL Constructions

```html
<!DOCTYPE html>
<html lang="en">
<head>
<meta charset="utf-8">
<title>BRL Constructions – Business Card</title>
<link rel="stylesheet" href="https://fonts.googleapis.com/css2?family=Michroma&family=Jura:wght@500;600&display=swap">
<style>
  :root {
    --backdrop: #8a8a8a;
    --card-charcoal: #3e3e3e;
    --card-red: #ea1c24;
    --divider: #e6e6e6;
    --ink-white: #ffffff;
    --ink-soft: #f2f2f2;
  }
  * { margin: 0; padding: 0; box-sizing: border-box; }
  html, body {
    width: 1200px;
    height: 852px;
    overflow: hidden;
    background: var(--backdrop);
  }
  .canvas {
    position: relative;
    width: 1200px;
    height: 852px;
  }
  .business-card {
    position: absolute;
    left: 232px;
    top: 187px;
    width: 758px;
    height: 464px;
    border-radius: 18px;
    overflow: hidden;
    background: var(--card-charcoal);
  }
  .brand {
    position: absolute;
    left: 0;
    right: 0;
    top: 150px;
    text-align: center;
    color: var(--ink-white);
    font-family: "Michroma", sans-serif;
    font-weight: 400;
  }
  .brand-name {
    display: block;
    font-size: 96px;
    line-height: 1;
    letter-spacing: 0.02em;
  }
  .brand-tagline {
    display: block;
    margin-top: 18px;
    font-size: 24px;
    line-height: 1;
    letter-spacing: 0.62em;
    padding-left: 0.62em;
  }
  .abn {
    position: absolute;
    left: 0;
    right: 0;
    top: 313px;
    text-align: center;
    color: var(--ink-soft);
    font-family: "Jura", sans-serif;
    font-weight: 600;
    font-size: 18px;
    letter-spacing: 0.04em;
  }
  .divider {
    position: absolute;
    left: 0;
    right: 0;
    top: 355px;
    height: 3px;
    background: var(--divider);
  }
  .contact-band {
    position: absolute;
    left: 0;
    right: 0;
    top: 358px;
    bottom: 0;
    background: var(--card-red);
    font-family: "Jura", sans-serif;
    font-weight: 600;
    color: var(--ink-white);
  }
  .holder-name {
    position: absolute;
    left: 36px;
    top: 36px;
    font-size: 25px;
    letter-spacing: 0.03em;
  }
  .contact-list {
    position: absolute;
    right: 34px;
    top: 14px;
    list-style: none;
  }
  .contact-item {
    display: flex;
    align-items: center;
    justify-content: flex-end;
    gap: 14px;
    height: 34px;
    font-size: 18px;
    letter-spacing: 0.06em;
  }
  .contact-icon { display: block; }
</style>
</head>
<body>
<main class="canvas">
  <section class="business-card" aria-label="BRL Constructions business card">
    <h1 class="brand">
      <span class="brand-name">BRL</span>
      <span class="brand-tagline">CONSTRUCTIONS</span>
    </h1>
    <p class="abn">ABN 12 345 678 910</p>
    <div class="divider"></div>
    <div class="contact-band">
      <p class="holder-name">YOUR NAME</p>
      <ul class="contact-list">
        <li class="contact-item">
          <span>0400 000 000</span>
          <svg class="contact-icon" width="22" height="34" viewBox="0 0 22 34" aria-hidden="true">
            <rect x="1.5" y="1.5" width="19" height="31" rx="3" fill="none" stroke="#fff" stroke-width="2"/>
            <line x1="2" y1="6.5" x2="20" y2="6.5" stroke="#fff" stroke-width="1.5"/>
            <line x1="2" y1="27" x2="20" y2="27" stroke="#fff" stroke-width="1.5"/>
            <circle cx="11" cy="30" r="1.2" fill="#fff"/>
          </svg>
        </li>
        <li class="contact-item">
          <span>EMAIL@EMAIL.COM.AU</span>
          <svg class="contact-icon" width="34" height="22" viewBox="0 0 34 22" aria-hidden="true">
            <rect x="0" y="0" width="34" height="22" rx="1.5" fill="#fff"/>
            <polyline points="1,1.5 17,13 33,1.5" fill="none" stroke="#ea1c24" stroke-width="2"/>
          </svg>
        </li>
      </ul>
    </div>
  </section>
</main>
</body>
</html>
```